Plakat-Design für Hypnose-Coaching
Zielgruppe
ich biete Hypnose-Sitzungen zur Auflösung des Glaubenssatzes 'Nicht gut genug?' Wir finden die Ursachen und lösen sie auf.
Meine Zielgruppe sind Frauen und teilweise auch Männer die sich im Berufsalltag aus Angst vor Zurückweisung oft unterordnen. Das, was sie sich fragen ist:
'Wieso schaffen es andere Menschen mit bestimmten Gesten oder Äußerungen, dass ich mich schlecht fühle?'
Aufgabenstellung
es soll ein DINA 4 Flyer werden.
'Nicht gut genug?'
Kindheitsmuster erkennen und auflösen
'Warum schaffen es andere Menschen mit Gesten oder Äußerungen, dass ich mich schlecht fühle?'
das war gestern! jetzt Termin vereinbaren: Hypnose-Coaching Henrik Dollmann Tel: 01563 8804257

```html
<!DOCTYPE html>
<html lang="de">
<head>
<meta charset="utf-8">
<title>Nicht gut genug? – Hypnose-Coaching</title>
<link rel="stylesheet" href="https://fonts.googleapis.com/css2?family=Fira+Sans:wght@400;600;700&display=swap">
<style>
  :root {
    --brand-blue: #1c55a0;
    --ink: #111111;
    --paper: #ffffff;
    --photo-grey: #9a9a9a;
    --photo-blue: #4a78b8;
  }
  html, body {
    margin: 0;
    padding: 0;
    width: 881px;
    height: 1200px;
    overflow: hidden;
    background: var(--paper);
  }
  .poster {
    position: relative;
    width: 881px;
    height: 1200px;
    background: var(--paper);
    font-family: "Fira Sans", Arial, sans-serif;
    color: var(--ink);
    overflow: hidden;
  }
  .hero-image {
    position: absolute;
    left: 0; top: 7px;
    width: 881px; height: 329px;
    background: linear-gradient(90deg, #8c8c8c 0%, #b5b5b5 35%, #d8dde6 55%, #6f93c6 75%, #3a68aa 100%);
  }
  .hero-rule {
    position: absolute;
    left: 0; top: 343px;
    width: 881px; height: 5px;
    background: var(--brand-blue);
  }
  .headline {
    position: absolute;
    left: 30px; top: 378px;
    margin: 0;
    font-size: 107px;
    font-weight: 600;
    line-height: 1;
    letter-spacing: -1px;
    color: var(--brand-blue);
    white-space: nowrap;
  }
  .subline {
    position: absolute;
    left: 36px; top: 508px;
    margin: 0;
    font-size: 38px;
    font-weight: 600;
    line-height: 1;
    white-space: nowrap;
  }
  .question {
    position: absolute;
    left: 38px; top: 604px;
    width: 440px;
    margin: 0;
    font-size: 31px;
    font-weight: 400;
    line-height: 44px;
  }
  .claim {
    position: absolute;
    left: 36px; top: 822px;
    margin: 0;
    font-size: 52px;
    font-weight: 600;
    line-height: 1;
    color: var(--brand-blue);
    white-space: nowrap;
  }
  .signpost {
    position: absolute;
    left: 523px; top: 611px;
    width: 338px; height: 345px;
    background: linear-gradient(160deg, #2c62ad 0%, #1c55a0 55%, #9aa3ad 100%);
    border-radius: 4px;
  }
  .portrait {
    position: absolute;
    left: 38px; top: 982px;
    width: 268px; height: 148px;
    background: linear-gradient(135deg, #c9ccd1 0%, #a88670 50%, #2a2a2e 100%);
  }
  .footer-band {
    position: absolute;
    left: 38px; top: 1142px;
    width: 843px; height: 58px;
    background: var(--brand-blue);
  }
  .certificate {
    position: absolute;
    left: 237px; top: 1047px;
    width: 132px; height: 132px;
  }
  .contact {
    position: absolute;
    left: 372px; top: 1041px;
    margin: 0;
    font-size: 26px;
    line-height: 32px;
    white-space: nowrap;
  }
  .contact-cta { font-weight: 600; display: block; }
  .contact-line { font-weight: 400; display: block; }
</style>
</head>
<body>
<main class="poster">
  <div class="hero-image" role="img" aria-label="Fotocollage im Puzzle-Stil: links ein bedrängter Jugendlicher in Graustufen, rechts ein niedergeschlagener Mann im blauen Hemd, auf den Finger zeigen"></div>
  <div class="hero-rule"></div>

  <h1 class="headline">Nicht gut genug?</h1>
  <p class="subline">Kindheitsmuster erkennen und auflösen</p>

  <p class="question">Warum schaffen es andere Menschen mit Gesten oder Äußerungen, dass ich mich schlecht fühle?</p>

  <p class="claim">Das war gestern!</p>

  <div class="signpost" role="img" aria-label="Foto eines Wegweisers mit blauen Schildern „Gestern“ und „Heute“ in entgegengesetzte Richtungen"></div>

  <div class="portrait" role="img" aria-label="Porträtfoto des Hypnose-Coachs Henrik Dollmann"></div>
  <div class="footer-band"></div>

  <svg class="certificate" viewBox="0 0 132 132" aria-hidden="true">
    <circle cx="66" cy="66" r="65" fill="#ffffff"/>
    <circle cx="66" cy="66" r="58" fill="#d9dde2" stroke="#8fa3b8" stroke-width="2"/>
    <circle cx="66" cy="66" r="34" fill="#2a8a94"/>
  </svg>

  <p class="contact">
    <span class="contact-cta">Jetzt Termin vereinbaren:</span>
    <span class="contact-line">Hypnose-Coaching Henrik Dollmann</span>
    <span class="contact-line">Tel: 01563 880 42 57</span>
  </p>
</main>
</body>
</html>
```